Business Cards for Harborline Estates Partners, Inc.
Business Cards, Stationary, Etc.
Professional
Rocco Tamberlini
Broker
4710 SE Marigold Commons Lane
Suite 100
Boca Raton, Fl 33867
rocco@harborlinepfl.com
We prefer the use of icons, as opposed to wording for phone, fax, email.
I will need 2 options for each submission. The second option should allow for a picture to be inserted on the business card.
*Upon completion the winning designer will need to send a 2nd set of files, for another agent in the office. - Name, title, contact info to follow upon conclusion of Contest.

```html
<!DOCTYPE html>
<html lang="en">
<head>
<meta charset="utf-8">
<title>Harborline Estates Partners, Inc. — Business Cards</title>
<link href="https://fonts.googleapis.com/css2?family=Open+Sans:ital,wght@0,400;0,600;0,700;1,400&display=swap" rel="stylesheet">
<style>
  :root {
    --board: #3b3b3d;
    --card: #ffffff;
    --navy: #2e3a5c;
    --ink: #5a5f6b;
    --label: #d9d9d9;
    --frame: #9a9ca2;
  }
  * { margin: 0; padding: 0; box-sizing: border-box; }
  html, body { width: 1200px; height: 809px; overflow: hidden; }
  body {
    background: var(--board);
    font-family: "Open Sans", Arial, sans-serif;
    position: relative;
  }
  .card {
    position: absolute;
    width: 499px;
    background: var(--card);
    border-radius: 14px;
    overflow: hidden;
  }
  .card--front { top: 43px; height: 312px; }
  .card--back { top: 432px; height: 276px; }
  .card--a { left: 72px; }
  .card--b { left: 636px; }

  .brand {
    position: absolute;
    left: 26px;
    top: 80px;
    display: flex;
    align-items: center;
    gap: 12px;
    white-space: nowrap;
  }
  .brand__mark {
    width: 40px; height: 40px;
    flex: none;
    background: var(--navy);
  }
  .brand__name {
    color: var(--navy);
    font-weight: 700;
    font-size: 19px;
    line-height: 1.1;
    letter-spacing: 0.4px;
  }

  .accent-strip {
    position: absolute;
    left: 0; top: 183px;
    width: 7px; height: 110px;
    background: var(--navy);
  }

  .contact {
    position: absolute;
    left: 34px; top: 188px;
    list-style: none;
    font-size: 10px;
    color: var(--ink);
    line-height: 14px;
  }
  .contact li { display: flex; align-items: flex-start; gap: 8px; }
  .contact li + li { margin-top: 2px; }
  .contact .gap { margin-top: 10px; }
  .contact svg { width: 10px; height: 10px; margin-top: 2px; flex: none; fill: var(--navy); }

  .agent {
    position: absolute;
    right: 22px; top: 284px;
    text-align: right;
    color: var(--ink);
    line-height: 13px;
  }
  .agent__name { font-style: italic; font-size: 12px; }
  .agent__title { font-size: 10px; }

  .photo-slot {
    position: absolute;
    right: 16px; top: 70px;
    width: 132px; height: 141px;
    border: 1.5px solid var(--frame);
    padding: 4px;
  }
  .photo-slot span { display: block; width: 100%; height: 100%; border: 1px solid var(--frame); }

  .brand--center {
    left: 50%; top: 50%;
    transform: translate(-50%, -50%);
    gap: 14px;
  }
  .brand--center .brand__mark { width: 58px; height: 58px; }
  .brand--center .brand__name { font-size: 26px; }

  .label {
    position: absolute;
    width: 499px;
    text-align: center;
    color: var(--label);
    font-size: 15px;
    letter-spacing: 3px;
    text-transform: uppercase;
  }
  .label--top { top: 360px; }
  .label--bottom { top: 716px; }
</style>
</head>
<body>

<section class="card card--front card--a">
  <div class="brand">
    <span class="brand__mark"></span>
    <span class="brand__name">HARBORLINE ESTATES<br>PARTNERS, INC.</span>
  </div>
  <span class="accent-strip"></span>
  <ul class="contact">
    <li><svg viewBox="0 0 10 10"><path d="M5 0.5 0.5 5H2v4.5h6V5h1.5z"/></svg><span>4710 SE Marigold Commons Lane<br>Suite 100 Boca Raton, Fl 33867</span></li>
    <li class="gap"><svg viewBox="0 0 10 10"><path d="M2 0.5h2l1 2.5-1.3 1a6 6 0 0 0 2.3 2.3l1-1.3 2.5 1v2A1 1 0 0 1 8.5 9.5 8 8 0 0 1 0.5 1.5 1 1 0 0 1 2 0.5z"/></svg><span>954-555-0142</span></li>
    <li><svg viewBox="0 0 10 10"><path d="M2 0.5h5v3H2zM0.5 4h9v4h-1.5v1.5h-6V8H0.5z"/></svg><span>561-555-0187</span></li>
    <li><svg viewBox="0 0 10 10"><path d="M0.5 2h9v6h-9zM1.2 2.6 5 5.6l3.8-3z" fill-rule="evenodd"/></svg><span>rocco@harborlinepfl.com</span></li>
  </ul>
  <div class="agent"><div class="agent__name">Rocco Tamberlini</div><div class="agent__title">Broker</div></div>
</section>
<p class="label label--top" style="left:72px">Business Card Front Option A</p>

<section class="card card--front card--b">
  <div class="brand">
    <span class="brand__mark"></span>
    <span class="brand__name">HARBORLINE ESTATES<br>PARTNERS, INC.</span>
  </div>
  <div class="photo-slot" role="img" aria-label="Space for agent photograph"><span></span></div>
  <span class="accent-strip"></span>
  <ul class="contact">
    <li><svg viewBox="0 0 10 10"><path d="M5 0.5 0.5 5H2v4.5h6V5h1.5z"/></svg><span>4710 SE Marigold Commons Lane<br>Suite 100 Boca Raton, Fl 33867</span></li>
    <li class="gap"><svg viewBox="0 0 10 10"><path d="M2 0.5h2l1 2.5-1.3 1a6 6 0 0 0 2.3 2.3l1-1.3 2.5 1v2A1 1 0 0 1 8.5 9.5 8 8 0 0 1 0.5 1.5 1 1 0 0 1 2 0.5z"/></svg><span>954-555-0142</span></li>
    <li><svg viewBox="0 0 10 10"><path d="M2 0.5h5v3H2zM0.5 4h9v4h-1.5v1.5h-6V8H0.5z"/></svg><span>561-555-0187</span></li>
    <li><svg viewBox="0 0 10 10"><path d="M0.5 2h9v6h-9zM1.2 2.6 5 5.6l3.8-3z" fill-rule="evenodd"/></svg><span>rocco@harborlinepfl.com</span></li>
  </ul>
  <div class="agent"><div class="agent__name">Rocco Tamberlini</div><div class="agent__title">Broker</div></div>
</section>
<p class="label label--top" style="left:636px">Business Card Front Option B</p>

<section class="card card--back card--a">
  <div class="brand brand--center">
    <span class="brand__mark"></span>
    <span class="brand__name">HARBORLINE ESTATES<br>PARTNERS, INC.</span>
  </div>
</section>
<p class="label label--bottom" style="left:72px">Business Card Front Option A</p>

<section class="card card--back card--b">
  <div class="brand brand--center">
    <span class="brand__mark"></span>
    <span class="brand__name">HARBORLINE ESTATES<br>PARTNERS, INC.</span>
  </div>
</section>
<p class="label label--bottom" style="left:636px">Business Card Front Option B</p>

</body>
</html>
```